The Wisdom of Lanterns New Book Cover Design Project

Book cover design . Paperback, ebook, and Talvora (derived from book cover) files/images required.
Book Title: The Wisdom of Lanterns
Subtitle: Under Copper Bridges
Author: Daniel Forsythe
Files: Ebook, Paperback (Brindlewick & Halvern Quill), Talvora sized image
File size & information to be provided once design is ready. Brindlewick paperback will be 5.25 x 8.
Completion date is flexible. Planning to publish in November.
Updates

Target Market(s)

Motorcycle owners

Font styles to use
Sans Serif

Requirements
Must have
• A generic looking motorcycle (samples attached). Thumbnail easily recognized as a motorcycle book.
Nice to have
• Open to all ideas but am favoring my idea: to emphasize the title lettering similar to (but not a copy of) other Wisdom books (examples attached), on a plain background. All books in the category have a motorcycle on the cover. Author name and subtitle do not have to be prominent. Rider optional..
Should not have
• Should not look like a biker romance or fantasy cover or look cartoonish. Motorcycle pic should be fairly generic (brand, style,).

```html
<!DOCTYPE html>
<html lang="en">
<head>
<meta charset="utf-8">
<title>The Wisdom of Lanterns — Daniel Forsythe</title>
<link rel="stylesheet" href="https://fonts.googleapis.com/css2?family=Bebas+Neue&family=Oswald:wght@600&display=swap">
<style>
  :root {
    --navy: #1b2156;
    --panel: rgba(40, 44, 96, 0.62);
    --white: #ffffff;
    --sky-top: #2f6fb8;
    --sky-mid: #a9c7e4;
    --cloud: #eef2f6;
    --hill: #4f7f3c;
    --road: #5d5f63;
    --chrome: #9aa4ad;
    --chrome-dark: #2a2e33;
  }
  * { margin: 0; padding: 0; box-sizing: border-box; }
  html, body { width: 801px; height: 1200px; overflow: hidden; background: var(--white); }
  .cover {
    position: relative;
    width: 801px;
    height: 1200px;
    overflow: hidden;
  }
  .cover-photo {
    position: absolute;
    inset: 0;
    background:
      radial-gradient(ellipse 60% 18% at 40% 12%, var(--cloud) 0%, rgba(238,242,246,0) 70%),
      radial-gradient(ellipse 50% 14% at 80% 20%, var(--cloud) 0%, rgba(238,242,246,0) 70%),
      linear-gradient(180deg,
        var(--sky-top) 0%,
        var(--sky-mid) 16%,
        var(--cloud) 24%,
        var(--hill) 30%,
        #6f9a45 40%,
        var(--road) 52%,
        #4a4c50 68%,
        var(--chrome) 76%,
        #d6dde3 82%,
        var(--chrome-dark) 92%,
        #4b4f55 100%);
  }
  .author {
    position: absolute;
    top: 132px;
    left: 0;
    width: 100%;
    text-align: center;
    font-family: "Oswald", sans-serif;
    font-weight: 600;
    font-size: 40px;
    letter-spacing: 0.5px;
    color: var(--navy);
    text-transform: uppercase;
  }
  .title-panel {
    position: absolute;
    left: 224px;
    top: 195px;
    width: 362px;
    height: 715px;
    background: var(--panel);
    border: 3px solid var(--white);
    display: flex;
    flex-direction: column;
    align-items: center;
    padding: 22px 14px 20px;
    color: var(--white);
    font-family: "Bebas Neue", sans-serif;
    text-transform: uppercase;
  }
  .title {
    display: flex;
    flex-direction: column;
    align-items: center;
    justify-content: space-between;
    flex: 1;
    line-height: 0.82;
    text-align: center;
  }
  .title-small { font-size: 86px; }
  .title-large { font-size: 136px; }
  .title-split { font-size: 160px; }
  .rule {
    width: 322px;
    height: 2px;
    background: var(--white);
    margin: 18px 0 14px;
  }
  .subtitle {
    font-family: "Bebas Neue", sans-serif;
    font-size: 36px;
    letter-spacing: 0.5px;
    line-height: 1;
  }
</style>
</head>
<body>
  <main class="cover">
    <div class="cover-photo" role="img" aria-label="Rider's view from a motorcycle: chrome handlebars and twin gauges in front, an open winding road through green hills under a bright blue sky with white clouds"></div>
    <p class="author">Daniel Forsythe</p>
    <section class="title-panel">
      <h1 class="title">
        <span class="title-small">The</span>
        <span class="title-large">Wisdom</span>
        <span class="title-small">Of</span>
        <span class="title-split">Lan</span>
        <span class="title-split">terns</span>
      </h1>
      <div class="rule"></div>
      <p class="subtitle">Under Copper Bridges</p>
    </section>
  </main>
</body>
</html>
```